Popup Banners - BrightCounsel - Legal Technology

- We need two banners (same style) designed with two different images and different text.

- The details of the printing requirements are attached, along with suggested images.

- The banners should share the same theme as our website www.brightcounsel.com.au

- The first banner would include our logo (attached), use the 'roads join' image (attached) in some way and text: New Opportunities - Where legal services and technology meet.

- The second banner would include our logo (attached), use the 'jigsaw' image (attached) in some way and use text: Legal Technology Strategy, Advice and Capability.

- Details on what are required from the Printer is attached also.

Target Market(s)

Legal Professionals

Industry/Entity Type

Information Technology

Font styles to use
Sans Serif

Requirements
Must have
• Our logo (attached), suggested text and the image mentioned for each.
Nice to have
• Professional and modern look
Should not have
• Cheap looking

```html
<!DOCTYPE html>
<html lang="en">
<head>
<meta charset="utf-8">
<title>BrightCounsel Pop-up Banners</title>
<link rel="stylesheet" href="https://fonts.googleapis.com/css2?family=Barlow:wght@400&display=swap">
<style>
  :root {
    --page: #ffffff;
    --banner: #ffffff;
    --ink: #5b5451;
    --headline-bg: #5b5451;
    --headline-text: #ffffff;
    --accent: #5aa0d0;
    --field-top: #6f9a45;
    --field-bottom: #55803a;
    --puzzle-top: #3f6a92;
    --puzzle-bottom: #2a4c70;
  }
  * { margin: 0; padding: 0; box-sizing: border-box; }
  html, body {
    width: 1200px; height: 1200px; overflow: hidden;
    background: var(--page);
    font-family: "Barlow", Arial, sans-serif;
  }
  .canvas { position: relative; width: 1200px; height: 1200px; }
  .banner {
    position: absolute; top: 75px;
    width: 403px; height: 993px;
    background: var(--banner);
    box-shadow: 0 6px 16px rgba(0, 0, 0, 0.13);
  }
  .banner--roads { left: 138px; }
  .banner--puzzle { left: 695px; }
  .brand {
    position: absolute; top: 36px; right: 34px;
    display: flex; align-items: center; gap: 12px;
    color: var(--ink);
    font-size: 24px; letter-spacing: 0.2em;
  }
  .brand__mark { width: 16px; height: 16px; background: var(--accent); }
  .headline {
    position: absolute; left: 22px; top: 157px;
    list-style: none;
  }
  .headline__line {
    display: block; width: fit-content;
    background: var(--headline-bg); color: var(--headline-text);
    font-size: 22px; line-height: 25px;
    padding: 0 2px; margin-bottom: 14px;
    text-transform: uppercase; letter-spacing: 0.01em;
    white-space: nowrap;
  }
  .headline__line--trail { padding-right: 18px; }
  .headline__line--wide { padding-right: 40px; }
  .graphics { position: absolute; left: 0; top: 0; width: 403px; height: 993px; }
</style>
</head>
<body>
<main class="canvas">

  <section class="banner banner--roads">
    <div class="brand"><span class="brand__mark"></span><span>BrightCounsel</span></div>
    <ul class="headline">
      <li class="headline__line headline__line--trail">New opportunities -</li>
      <li class="headline__line">Where legal services</li>
      <li class="headline__line">and technology come together</li>
    </ul>
    <svg class="graphics" viewBox="0 0 403 993">
      <defs>
        <linearGradient id="roadsFill" x1="0" y1="0" x2="0" y2="1">
          <stop offset="0" stop-color="var(--field-top)"/>
          <stop offset="1" stop-color="var(--field-bottom)"/>
        </linearGradient>
      </defs>
      <polygon points="329,372 403,372 403,433 283,433" fill="var(--accent)"/>
      <polygon role="img" aria-label="Photo: two country roads joining across a grassy hill"
               points="276,440 403,440 403,710 284,874 0,874 0,806" fill="url(#roadsFill)"/>
      <polygon points="0,881 275,881 242,931 0,931" fill="var(--accent)"/>
    </svg>
  </section>

  <section class="banner banner--puzzle">
    <div class="brand"><span class="brand__mark"></span><span>BrightCounsel</span></div>
    <ul class="headline">
      <li class="headline__line headline__line--wide">Legal technology strategy,</li>
      <li class="headline__line">Advice and capability</li>
    </ul>
    <svg class="graphics" viewBox="0 0 403 993">
      <defs>
        <linearGradient id="puzzleFill" x1="0" y1="0" x2="0" y2="1">
          <stop offset="0" stop-color="var(--puzzle-top)"/>
          <stop offset="1" stop-color="var(--puzzle-bottom)"/>
        </linearGradient>
      </defs>
      <polygon points="329,372 403,372 403,433 283,433" fill="var(--accent)"/>
      <polygon role="img" aria-label="Photo: a hand placing a lit jigsaw puzzle piece"
               points="276,440 403,440 403,710 284,874 0,874 0,806" fill="url(#puzzleFill)"/>
      <polygon points="0,881 275,881 242,931 0,931" fill="var(--accent)"/>
    </svg>
  </section>

</main>
</body>
</html>
```